Plump Wally's Terrier Store - balms

We are looking for a logo design for our new Bulldog butter tins and website. Inspired by our little fat bulldog Wally who has very sensitive skin issues we have scoured the earth to find something for him - turns out only the most natural of ingredients suits our boy so we set out to get something made just for him. All natural, all organic and want to share it with other dogs and their mums and dads.

Wally is a red and white bulldog and we really would like a design that is as close to resembling him as possible. See logo image below - but with Wally and smiling! Essential the face markings are captured as much as possible (e.g. the dot on his head, eye patch etc). Options to see either just face or something similar to the pic titled Mossbrook.

Important to convey natural and organic colouring. Organic type symbol.

Classy upmarket look. Eyecatching. Strong branding potential. see the meadow hound works http://meadowhoundworks.example/shop/ as an example of simple but classy.

Logo to include wording Mossbrook, 100% Natural & Organic, Terrier Salve.

Some photos included below of Wally. Can also be seen on instagram @plumpwallytheterrier.

Tin will be similar to surfers wax - Dad is a surfer and so is Wally! Rectangular. Estimated dimensions 110mmx80mmx25mm (see similar image).
Thank you!

Target Market(s)

Pet owners who adore their pet babies!

Industry/Entity Type

Shop

Requirements
Must have
• Be designed for a rectangular tin Estimated dimensions 110mmx80mmx25mm. Landscape view
• Organic logo (see file upload) located in corner.
• Net Wt 50gm
• Classy upmarket look but simple. Eyecatching. Not too cartoonish.
• Logo to include wording Mossbrook, 100% Organic, Skin Balm
• Must capture Wally's facemarkings - dot on head, eye patch, dots around nose and mouth.
• Key colours of Wally (reddy-brown & tan /black and white) - probably don't want too many other colours - keep simple and classy
• Looking for a coloured background for the label - potentially same colour as Wally to give a kind of a natural feel.
Should not have
• design for a round tin

```html
<!DOCTYPE html>
<html lang="en">
<head>
<meta charset="utf-8">
<title>Mossbrook – Skin Balm Identity</title>
<link rel="stylesheet" href="https://fonts.googleapis.com/css2?family=Montserrat:wght@700&display=swap">
<style>
  :root {
    --paper: #f0efed;
    --brown: #5b3326;
    --mint: #aadbc1;
    --white: #ffffff;
    --pup-white: #f4f2ee;
    --pup-brown: #7a3e2a;
    --badge: #e7f3df;
    --badge-edge: #5aa844;
  }
  * { box-sizing: border-box; margin: 0; padding: 0; }
  html, body { width: 1200px; height: 2308px; overflow: hidden; }
  body {
    background: var(--paper);
    position: relative;
    font-family: "Montserrat", sans-serif;
    font-weight: 700;
    color: var(--brown);
  }

  .pup-art {
    position: absolute;
    border-radius: 38% 38% 46% 46%;
    background: linear-gradient(100deg, var(--pup-white) 0%, var(--pup-white) 48%, var(--pup-brown) 52%, var(--pup-brown) 100%);
  }

  .wordmark {
    position: absolute;
    font-family: "Montserrat", sans-serif;
    font-weight: 700;
    color: var(--brown);
    letter-spacing: 4px;
    line-height: 1;
    white-space: nowrap;
    text-transform: uppercase;
  }
  .tagline {
    position: absolute;
    font-weight: 700;
    color: var(--brown);
    letter-spacing: 3px;
    text-transform: uppercase;
    white-space: nowrap;
    line-height: 1;
  }

  /* stacked logo */
  .logo-stacked .pup-art { left: 513px; top: 56px; width: 174px; height: 258px; }
  .logo-stacked .wordmark { left: 0; width: 1200px; text-align: center; top: 332px; font-size: 64px; }
  .logo-stacked .tagline { left: 0; width: 1200px; text-align: center; top: 414px; font-size: 24px; }

  /* horizontal logo */
  .logo-inline .pup-art { left: 240px; top: 496px; width: 186px; height: 260px; }
  .logo-inline .wordmark { left: 452px; top: 605px; font-size: 64px; }
  .logo-inline .tagline { left: 454px; top: 684px; font-size: 24px; }

  /* tin label */
  .tin-label {
    position: absolute;
    left: 157px;
    width: 886px;
    height: 641px;
    background: var(--brown);
    padding: 15px;
  }
  .tin-label--front { top: 790px; }
  .tin-label--repeat { top: 1500px; }
  .tin-label__face {
    position: relative;
    width: 100%;
    height: 100%;
    border: 5px solid var(--white);
    background: var(--mint);
  }
  .tin-label__dash {
    position: absolute;
    inset: 30px;
    border: 2px dashed var(--white);
  }
  .paw {
    position: absolute;
    left: 50%;
    top: 24px;
    width: 40px;
    height: 36px;
    transform: translateX(-50%);
  }
  .label-claim {
    position: absolute;
    left: 0; width: 100%;
    top: 76px;
    text-align: center;
    font-size: 22px;
    letter-spacing: 1px;
    line-height: 1;
    color: var(--brown);
  }
  .tin-label .pup-art { left: 325px; top: 166px; width: 196px; height: 272px; }
  .tin-label .wordmark { left: 0; width: 100%; text-align: center; top: 462px; font-size: 56px; }

  .ribbon {
    position: absolute;
    top: 244px;
    width: 266px;
    height: 122px;
  }
  .ribbon svg { position: absolute; inset: 0; width: 100%; height: 100%; }
  .ribbon__text {
    position: absolute;
    top: 0; height: 100%;
    display: flex; align-items: center; justify-content: center;
    color: var(--white);
    font-size: 28px;
    letter-spacing: 1px;
    line-height: 1.15;
    text-align: center;
    text-transform: uppercase;
  }
  .ribbon--left { left: -20px; }
  .ribbon--left .ribbon__text { left: 10px; width: 210px; }
  .ribbon--right { right: -20px; }
  .ribbon--right .ribbon__text { left: 50px; width: 200px; }

  .cert-badge {
    position: absolute;
    right: 67px;
    bottom: 50px;
    width: 110px;
    height: 55px;
    background: var(--badge);
    border: 3px solid var(--badge-edge);
    border-radius: 6px;
  }
</style>
</head>
<body>

  <section class="logo-stacked">
    <div class="pup-art" role="img" aria-label="Illustrated face of a red and white terrier, tongue out, with eye patch and nose spots"></div>
    <div class="wordmark">Mossbrook</div>
    <div class="tagline">100% Organic, Skin Balm</div>
  </section>

  <section class="logo-inline">
    <div class="pup-art" role="img" aria-label="Illustrated face of a red and white terrier, tongue out, with eye patch and nose spots"></div>
    <div class="wordmark">Mossbrook</div>
    <div class="tagline">100% Organic, Skin Balm</div>
  </section>

  <section class="tin-label tin-label--front">
    <div class="tin-label__face">
      <div class="tin-label__dash"></div>
      <svg class="paw" viewBox="0 0 44 40" aria-hidden="true">
        <g fill="#ffffff">
          <ellipse cx="22" cy="29" rx="11" ry="9"/>
          <ellipse cx="7" cy="17" rx="4.5" ry="5.5"/>
          <ellipse cx="16" cy="8" rx="4.5" ry="6"/>
          <ellipse cx="28" cy="8" rx="4.5" ry="6"/>
          <ellipse cx="37" cy="17" rx="4.5" ry="5.5"/>
        </g>
      </svg>
      <div class="label-claim">100% ORGANIC</div>
      <div class="ribbon ribbon--left">
        <svg viewBox="0 0 266 122" preserveAspectRatio="none"><polygon points="0,3 263,3 228,61 263,119 0,119" fill="#5b3326" stroke="#ffffff" stroke-width="5"/></svg>
        <div class="ribbon__text">Skin<br>Balm</div>
      </div>
      <div class="ribbon ribbon--right">
        <svg viewBox="0 0 266 122" preserveAspectRatio="none"><polygon points="3,3 266,3 266,119 3,119 38,61" fill="#5b3326" stroke="#ffffff" stroke-width="5"/></svg>
        <div class="ribbon__text">50 GM</div>
      </div>
      <div class="pup-art" role="img" aria-label="Illustrated face of a red and white terrier, tongue out, with eye patch and nose spots"></div>
      <div class="wordmark">Mossbrook</div>
      <div class="cert-badge" role="img" aria-label="Organic certification badge"></div>
    </div>
  </section>

  <section class="tin-label tin-label--repeat">
    <div class="tin-label__face">
      <div class="tin-label__dash"></div>
      <svg class="paw" viewBox="0 0 44 40" aria-hidden="true">
        <g fill="#ffffff">
          <ellipse cx="22" cy="29" rx="11" ry="9"/>
          <ellipse cx="7" cy="17" rx="4.5" ry="5.5"/>
          <ellipse cx="16" cy="8" rx="4.5" ry="6"/>
          <ellipse cx="28" cy="8" rx="4.5" ry="6"/>
          <ellipse cx="37" cy="17" rx="4.5" ry="5.5"/>
        </g>
      </svg>
      <div class="label-claim">100% ORGANIC</div>
      <div class="ribbon ribbon--left">
        <svg viewBox="0 0 266 122" preserveAspectRatio="none"><polygon points="0,3 263,3 228,61 263,119 0,119" fill="#5b3326" stroke="#ffffff" stroke-width="5"/></svg>
        <div class="ribbon__text">Skin<br>Balm</div>
      </div>
      <div class="ribbon ribbon--right">
        <svg viewBox="0 0 266 122" preserveAspectRatio="none"><polygon points="3,3 266,3 266,119 3,119 38,61" fill="#5b3326" stroke="#ffffff" stroke-width="5"/></svg>
        <div class="ribbon__text">50 GM</div>
      </div>
      <div class="pup-art" role="img" aria-label="Illustrated face of a red and white terrier, tongue out, with eye patch and nose spots"></div>
      <div class="wordmark">Mossbrook</div>
      <div class="cert-badge" role="img" aria-label="Organic certification badge"></div>
    </div>
  </section>

</body>
</html>
```